Up to the Challenge? Canadian based consulting company needs a two sided business card design

A Canadian based security risk management consulting company needs a two-sided business card design. What we do is provide advice and guidance related to emergency, security and business continuity management for small, medium and large companies to help ensure the protection of their people, assets, information, services, operations and reputation.

The final design should be simple, only one or two colours, eye catching, professional and one that makes people look at three or more times just because it looks so darn good.

I have include examples of business cards I like.

Target Market(s)

Small, medium and large companies.

Industry/Entity Type

Security

Contact Information for Business Card

Business Card Size: Standard size of 3.5" (89mm) x 2.0" (51mm) - (see full specifications and guides on PRINTA's website if required)
Card Stock: Looking to use PRINTA's Velda 32pt stock textured paper - seam colour either chili red or black
Business Name: The Harrowfield Group
Website: www.theharrowfieldgroup.example
Telephone: (555)214-0397
Name: Dana Forsythe
Position: Principle
e-mail: Dana.Forsythe@theharrowfieldgroup.example

Font styles to use
Serif

Colors
ec1f27
000000
9d9d9d
aaaaaa
606060

Requirements
Must have
• - "The Harrowfield Group" logo (see uploaded files). I have included grey scale and colour versions.
• - Business card details (as above)
Nice to have
• - One side black or grey scale.
• - Other side would likely be white.
• - Everyone likes the silver logo on the black background.
• - Small element of colour i.e. red but I'm leaning more to greyscale.
Should not have
• - A lot of colour. Keep it simple.

```html
<!DOCTYPE html>
<html lang="en">
<head>
<meta charset="utf-8">
<title>The Harrowfield Group — Business Card</title>
<link rel="stylesheet" href="https://fonts.googleapis.com/css2?family=Cinzel:wght@400;500&family=Raleway:wght@400;500&display=swap">
<style>
  :root {
    --stage: #e9e7e4;
    --card-dark: #58585a;
    --card-dark-emboss: #6c6c6e;
    --card-light: #ffffff;
    --ink: #606060;
    --ink-soft: #7a7a7a;
    --accent: #ec1f27;
    --silver-1: #d4d4d4;
    --silver-2: #9d9d9d;
    --rule: #aaaaaa;
  }
  html, body {
    margin: 0;
    padding: 0;
    width: 1200px;
    height: 900px;
    overflow: hidden;
    background: var(--stage);
  }
  .canvas {
    position: relative;
    width: 1200px;
    height: 900px;
  }
  .card {
    position: absolute;
    left: 250px;
    width: 700px;
    height: 400px;
    border-radius: 26px;
    overflow: hidden;
    box-shadow: 0 10px 28px rgba(0,0,0,0.18);
  }
  .card--front { top: 40px; background: var(--card-dark); }
  .card--back  { top: 460px; background: var(--card-light); }

  .motif-area {
    position: absolute;
    left: 0;
    bottom: 0;
    width: 170px;
    height: 150px;
  }
  .card--front .motif-area {
    background: radial-gradient(ellipse at 20% 80%, rgba(157,157,157,0.45), rgba(157,157,157,0) 70%);
  }
  .card--back .motif-area {
    width: 220px;
    height: 190px;
    background: radial-gradient(ellipse at 25% 85%, rgba(157,157,157,0.55), rgba(212,212,212,0.2) 55%, rgba(255,255,255,0) 75%);
  }

  .wordmark {
    position: absolute;
    right: 48px;
    top: 150px;
    display: flex;
    align-items: center;
    gap: 16px;
    color: var(--card-dark-emboss);
    font-family: "Cinzel", serif;
    font-weight: 500;
  }
  .wordmark__square {
    width: 34px;
    height: 34px;
    background: var(--card-dark-emboss);
  }
  .wordmark__text { text-align: center; line-height: 1; }
  .wordmark__name { font-size: 34px; letter-spacing: 1px; }
  .wordmark__sub { font-size: 20px; letter-spacing: 6px; margin-top: 6px; }

  .contact {
    position: absolute;
    right: 40px;
    top: 205px;
    font-family: "Raleway", sans-serif;
    color: var(--ink);
  }
  .contact__header {
    border-left: 3px solid var(--accent);
    padding-left: 12px;
  }
  .contact__name {
    font-family: "Cinzel", serif;
    font-size: 22px;
    letter-spacing: 1px;
    color: var(--ink);
    margin: 0;
  }
  .contact__role {
    font-size: 16px;
    color: var(--ink-soft);
    margin: 2px 0 0;
  }
  .contact__list {
    list-style: none;
    margin: 10px 0 0 30px;
    padding: 0 0 0 10px;
    border-left: 2px solid var(--rule);
  }
  .contact__item {
    display: flex;
    align-items: center;
    gap: 8px;
    font-size: 15px;
    line-height: 24px;
  }
  .contact__icon { width: 12px; height: 12px; flex: none; }
</style>
</head>
<body>
<main class="canvas">

  <section class="card card--front" aria-label="Card front">
    <div class="motif-area" role="img" aria-label="Faint brand leaf motif area"></div>
    <div class="wordmark">
      <span class="wordmark__square"></span>
      <div class="wordmark__text">
        <div class="wordmark__name">THE HARROWFIELD</div>
        <div class="wordmark__sub">GROUP</div>
      </div>
    </div>
  </section>

  <section class="card card--back" aria-label="Card back">
    <div class="motif-area" role="img" aria-label="Silver brand leaf motif area"></div>
    <div class="contact">
      <div class="contact__header">
        <p class="contact__name">DANA FORSYTHE</p>
        <p class="contact__role">Principle</p>
      </div>
      <ul class="contact__list">
        <li class="contact__item">
          <svg class="contact__icon" viewBox="0 0 12 12" aria-hidden="true"><path fill="#ec1f27" d="M2.5 0.8l2 2-1 1.2c.6 1.4 1.9 2.8 3.4 3.5l1.2-1 2 2-1.3 1.7C4.8 9.8 2 7 .9 2.1z"/></svg>
          (555) 214-0397
        </li>
        <li class="contact__item">
          <svg class="contact__icon" viewBox="0 0 12 12" aria-hidden="true"><rect x="0.5" y="2.5" width="11" height="7.5" fill="#ec1f27"/><path d="M0.8 2.8L6 6.8l5.2-4" stroke="#fff" stroke-width="1" fill="none"/></svg>
          Dana.Forsythe@theharrowfieldgroup.example
        </li>
        <li class="contact__item">
          <svg class="contact__icon" viewBox="0 0 12 12" aria-hidden="true"><circle cx="6" cy="6" r="5.2" fill="#ec1f27"/><path d="M0.8 6h10.4M6 0.8c-2.4 2.8-2.4 7.6 0 10.4M6 0.8c2.4 2.8 2.4 7.6 0 10.4" stroke="#fff" stroke-width="0.8" fill="none"/></svg>
          www.theharrowfieldgroup.example
        </li>
      </ul>
    </div>
  </section>

</main>
</body>
</html>
```